Postcard needed for expert witness service

Looking for a professional postcard that will be mailed to personal injury lawyers / law firms to introduce my expert witness services.

Target Market(s)

Law firms, personal injury lawyers

Industry/Entity Type

Expert witness, law

Font styles to use
Sans Serif

Requirements
Must have
• Logo: The Frost Counsel [Main Heading]Do you handle snow and ice related slip and falls? Darrel is one of the top snow industry experts in the country! [Following should be in a list type fashion, possibly bulleted]Darrel's credentials: Accredited Winter Practitioner (AWP), past WRTA board member and chair, former ISO 9001 certified snow company owner , 32 years in the industry. (555) 284-3917 NOTES: Postcard will be 4" x 6" Please use both sides however must have room for labels and stamp
Should not have
• Wouldn't suggest using both photos on same side. Honestly, feel free to only use one of the slip and fall photos if it works out better. Thanks!

```html
<!DOCTYPE html>
<html lang="en">
<head>
<meta charset="utf-8">
<title>The Frost Counsel – Postcard</title>
<link rel="stylesheet" href="https://fonts.googleapis.com/css2?family=Poppins:wght@300;400;500;600;800&display=swap">
<style>
  :root {
    --page-bg: #e4e4e4;
    --card-white: #ffffff;
    --ink: #161c20;
    --blue: #0a8ac4;
    --blue-bright: #1aa7e6;
    --text-white: #ffffff;
    --muted: #2a2f33;
  }
  * { box-sizing: border-box; margin: 0; padding: 0; }
  html, body { width: 1200px; height: 1185px; overflow: hidden; }
  body { background: var(--page-bg); font-family: "Poppins", sans-serif; position: relative; }

  .card {
    position: absolute; left: 220px; width: 760px; height: 506px;
    background: var(--card-white); overflow: hidden;
    box-shadow: 0 6px 18px rgba(0,0,0,0.12);
  }
  .card--front { top: 77px; }
  .card--back { top: 604px; }

  /* Wordmark */
  .wordmark {
    position: absolute; font-family: "Poppins", sans-serif; font-weight: 300;
    color: var(--ink); text-transform: uppercase; line-height: 1;
    display: flex; flex-direction: column; align-items: center;
  }
  .wordmark__top { letter-spacing: 1px; }
  .wordmark__bottom { letter-spacing: 0.3em; margin-top: 4px; }
  .card--front .wordmark { left: 41px; top: 40px; }
  .card--front .wordmark__top { font-size: 38px; }
  .card--front .wordmark__bottom { font-size: 20px; }

  /* Front */
  .hero-photo {
    position: absolute; left: 300px; top: 0; width: 460px; height: 350px;
    background:
      linear-gradient(90deg, #ffffff 0%, rgba(255,255,255,0) 35%),
      linear-gradient(160deg, #9c958d 0%, #d9d7d3 40%, #5b5a60 60%, #e6e6e6 100%);
  }
  .headline {
    position: absolute; left: 41px; top: 125px;
    font-weight: 800; font-size: 36.5px; line-height: 37px; letter-spacing: -0.5px;
    text-transform: uppercase; color: var(--ink);
  }
  .headline__accent { color: var(--blue); }

  .front-band { position: absolute; left: 0; top: 349px; width: 760px; height: 157px; background: var(--ink); }
  .front-banner {
    position: absolute; left: 200px; top: 310px; width: 517px; height: 82px;
    background: var(--blue); border-top-right-radius: 36px;
  }
  .front-banner__text {
    position: absolute; left: 20px; top: 14px; color: var(--text-white);
    font-weight: 800; font-size: 23.5px; line-height: 28px; text-transform: uppercase; letter-spacing: -0.3px;
  }
  .portrait {
    position: absolute; left: 43px; top: 311px; width: 160px; height: 160px; border-radius: 50%;
    border: 4px solid var(--blue);
    background: radial-gradient(circle at 50% 45%, #c9ced4 0%, #e9ecef 60%, #f4f5f6 100%);
  }
  .call {
    position: absolute; font-weight: 800; text-transform: uppercase; color: var(--blue-bright);
    letter-spacing: -0.5px; white-space: nowrap;
  }
  .call__number { color: var(--text-white); font-weight: 600; text-transform: none; letter-spacing: -0.5px; }
  .card--front .call { left: 220px; top: 407px; font-size: 31px; }

  /* Back */
  .cred-panel {
    position: absolute; left: 0; top: 0; width: 381px; height: 410px;
    background:
      linear-gradient(180deg, rgba(10,138,196,1) 0%, rgba(10,138,196,0.96) 55%, rgba(40,150,205,0.85) 100%),
      linear-gradient(90deg, #6b8ca5, #2b4c68);
  }
  .cred-title {
    position: absolute; left: 41px; top: 50px; color: var(--text-white);
    font-weight: 800; font-size: 38px; line-height: 41px; text-transform: uppercase; letter-spacing: -0.3px;
  }
  .cred-list { position: absolute; left: 41px; top: 144px; width: 335px; list-style: none; color: var(--text-white); }
  .cred-list__item {
    position: relative; padding-left: 24px; font-weight: 500; font-size: 19.5px; line-height: 27px;
    margin-bottom: 8px; letter-spacing: -0.2px;
  }
  .cred-list__tick { position: absolute; left: 0; top: 6px; width: 15px; height: 15px; }
  .back-band { position: absolute; left: 0; top: 410px; width: 381px; height: 96px; background: var(--ink); }
  .card--back .call { left: 41px; top: 433px; font-size: 23.5px; }

  .mail-side { position: absolute; left: 381px; top: 0; width: 379px; height: 506px; background: var(--card-white); }
  .mail-side .wordmark { left: 24px; top: 50px; }
  .mail-side .wordmark__top { font-size: 30px; }
  .mail-side .wordmark__bottom { font-size: 15px; }
  .contact { position: absolute; left: 24px; top: 106px; list-style: none; color: var(--muted); font-size: 10.5px; font-weight: 500; }
  .contact__line { display: flex; align-items: center; gap: 4px; height: 18px; }
  .contact__icon { width: 10px; height: 10px; }
</style>
</head>
<body>

<section class="card card--front">
  <div class="hero-photo" role="img" aria-label="Photo of a woman in a winter coat and knit hat falling on an icy, snowy pavement"></div>
  <div class="wordmark"><span class="wordmark__top">The Frost</span><span class="wordmark__bottom">Counsel</span></div>
  <h1 class="headline">Do you handle<br><span class="headline__accent">snow and<br>ice related slip<br>and falls?</span></h1>
  <div class="front-band"></div>
  <div class="front-banner"><p class="front-banner__text">Darrel is one of the top snow<br>industry experts in the country!</p></div>
  <div class="portrait" role="img" aria-label="Portrait photo of Darrel in a light blue shirt"></div>
  <p class="call">Call now! <span class="call__number">(555) 284-3917</span></p>
</section>

<section class="card card--back">
  <div class="cred-panel" role="img" aria-label="Faded blue-tinted photo of a person slipping on an icy street"></div>
  <h2 class="cred-title">Darrel's<br>credentials:</h2>
  <ul class="cred-list">
    <li class="cred-list__item"><svg class="cred-list__tick" viewBox="0 0 16 16"><circle cx="8" cy="8" r="8" fill="#fff"/><path d="M4.5 8.2l2.3 2.3 4.7-4.8" fill="none" stroke="#0a8ac4" stroke-width="2" stroke-linecap="round" stroke-linejoin="round"/></svg>Accredited Winter Practitioner (AWP)</li>
    <li class="cred-list__item"><svg class="cred-list__tick" viewBox="0 0 16 16"><circle cx="8" cy="8" r="8" fill="#fff"/><path d="M4.5 8.2l2.3 2.3 4.7-4.8" fill="none" stroke="#0a8ac4" stroke-width="2" stroke-linecap="round" stroke-linejoin="round"/></svg>Past WRTA board member and chair</li>
    <li class="cred-list__item"><svg class="cred-list__tick" viewBox="0 0 16 16"><circle cx="8" cy="8" r="8" fill="#fff"/><path d="M4.5 8.2l2.3 2.3 4.7-4.8" fill="none" stroke="#0a8ac4" stroke-width="2" stroke-linecap="round" stroke-linejoin="round"/></svg>Former ISO 9001 certified snow company owner</li>
    <li class="cred-list__item"><svg class="cred-list__tick" viewBox="0 0 16 16"><circle cx="8" cy="8" r="8" fill="#fff"/><path d="M4.5 8.2l2.3 2.3 4.7-4.8" fill="none" stroke="#0a8ac4" stroke-width="2" stroke-linecap="round" stroke-linejoin="round"/></svg>32 years in the industry.</li>
  </ul>
  <div class="back-band"></div>
  <p class="call">Call now! <span class="call__number">(555) 284-3917</span></p>

  <div class="mail-side">
    <div class="wordmark"><span class="wordmark__top">The Frost</span><span class="wordmark__bottom">Counsel</span></div>
    <ul class="contact">
      <li class="contact__line">P.O. Box 118, Lakeview MI 49001</li>
      <li class="contact__line"><svg class="contact__icon" viewBox="0 0 10 10"><circle cx="5" cy="5" r="5" fill="#0a8ac4"/><circle cx="5" cy="5" r="2.6" fill="none" stroke="#fff" stroke-width="0.9"/></svg>www.frostcounsel-mail.com</li>
      <li class="contact__line"><svg class="contact__icon" viewBox="0 0 10 10"><circle cx="5" cy="5" r="5" fill="#0a8ac4"/><rect x="2.5" y="3.3" width="5" height="3.4" fill="#fff"/></svg>darrel@frostcounsel-mail.com</li>
    </ul>
  </div>
</section>

</body>
</html>
```